Design for a Note buying company that attracts landlords and seller financed notes

I need a card designed. I want a simple clean front with my logo and contact info. On the back I want some big and bold words to get a message across.

Our Company buys Notes (mortgages) and we want to convey the sense of financial security. Our number one market that we pursue is tired landlords.

If you want to understand our business you can visit our website. www.deedpaperlane.com

Do not use any Clip Art in the design, it will not be accepted. I want a custom designed card not something I could throw together myself. Simple clean and drive the message home.

Target Market(s)

Landlords, seller financed note holders

Industry/Entity Type

Mortgage

Contact Information for Business Card

Simple clean and bold. I need to grab the attention of the customer. It should convey a professional touch.

Font styles to use
Sans Serif

Colors
ec2229
ffffff

Requirements
Must have
• Clean front with logo and contact information
Front colors should match logo

Back should be bold and grab attention. Back colors are open to ideas
Nice to have
• The Back May use the phrase "No more Tentants, No more Toilets" "More Time, More Cash"

I'm open to other ideas about grabbing a landlords attention

I'm open to a square card design
I like cards with round corners as well
Should not have
• any clip art! must be custom designs.

```html
<!DOCTYPE html>
<html lang="en">
<head>
<meta charset="utf-8">
<title>Deedpaper Note Buyers – Business Card</title>
<link rel="stylesheet" href="https://fonts.googleapis.com/css2?family=Exo+2:wght@600;700;800&family=Arimo:wght@400;700&display=swap">
<style>
  :root {
    --brand-red: #ec2229;
    --card-white: #ffffff;
    --card-black: #000000;
    --ink: #1a1a1a;
    --stage: #4d4d4d;
  }
  * { box-sizing: border-box; margin: 0; padding: 0; }
  html, body { width: 1200px; height: 900px; overflow: hidden; }
  body { background: var(--stage); position: relative; font-family: "Arimo", Arial, sans-serif; }

  .card {
    position: absolute;
    top: 259px;
    width: 393px;
    height: 393px;
    border: 8px solid var(--brand-red);
    box-shadow: 4px 5px 6px rgba(0,0,0,0.55);
  }
  .card--front { left: 198px; background: var(--card-white); }
  .card--back { left: 613px; background: var(--card-black); border-width: 10px; }

  /* Front */
  .front-brand {
    position: absolute;
    left: 14px;
    top: 63px;
    width: 84px;
    height: 250px;
    display: flex;
    align-items: center;
    justify-content: center;
  }
  .front-brand__name {
    transform: rotate(-90deg);
    font-family: "Exo 2", sans-serif;
    font-weight: 800;
    font-size: 40px;
    color: var(--card-black);
    white-space: nowrap;
    letter-spacing: 1px;
  }
  .contact { position: absolute; left: 124px; top: 96px; color: var(--ink); }
  .contact__name {
    font-weight: 700;
    font-size: 20px;
    color: var(--brand-red);
    letter-spacing: 0.8px;
    line-height: 24px;
  }
  .contact__role { font-size: 17px; line-height: 22px; margin-bottom: 10px; }
  .contact__list { list-style: none; }
  .contact__item {
    display: flex;
    align-items: center;
    gap: 4px;
    font-size: 17.5px;
    line-height: 25px;
    margin-left: -4px;
  }
  .contact__icon { width: 23px; height: 23px; flex: none; }
  .contact__address { font-size: 17.5px; line-height: 24px; margin-top: 12px; }

  /* Back */
  .back { position: absolute; inset: 0; text-align: center; color: var(--card-white); font-family: "Exo 2", sans-serif; }
  .back__tagline {
    position: absolute; left: 0; right: 0; top: 41px;
    font-size: 13px; font-weight: 700; letter-spacing: 4.4px;
  }
  .back__brand {
    position: absolute; left: 0; right: 0; top: 76px;
    font-size: 48px; font-weight: 800; letter-spacing: 1.5px; line-height: 56px;
  }
  .back__descriptor {
    position: absolute; left: 0; right: 0; top: 149px;
    font-size: 21px; font-weight: 700; letter-spacing: 4.6px;
  }
  .back__message {
    position: absolute; left: 0; right: 0; top: 213px;
    font-size: 29px; font-weight: 700; line-height: 35px;
  }
  .back__message--cash { top: 296px; }
</style>
</head>
<body>
  <section class="card card--front" aria-label="Card front">
    <div class="front-brand">
      <span class="front-brand__name">DEEDPAPER</span>
    </div>
    <div class="contact">
      <p class="contact__name">DANIEL HARPER</p>
      <p class="contact__role">Managing Director</p>
      <ul class="contact__list">
        <li class="contact__item">
          <svg class="contact__icon" viewBox="0 0 24 24" aria-hidden="true">
            <circle cx="12" cy="12" r="10" fill="none" stroke="#ec2229" stroke-width="2"/>
            <path d="M8.5 6.5l2 2-1.2 1.6c.8 1.8 2.2 3.2 4 4l1.6-1.2 2 2-1.5 1.8c-3.8-.6-7.5-4.3-8.1-8.1z" fill="#ec2229"/>
          </svg>
          <span>044-555 018 272</span>
        </li>
        <li class="contact__item">
          <svg class="contact__icon" viewBox="0 0 24 24" aria-hidden="true">
            <circle cx="12" cy="12" r="11" fill="#ec2229"/>
            <rect x="6" y="8" width="12" height="8.5" fill="none" stroke="#fff" stroke-width="1.4"/>
            <path d="M6 8l6 5 6-5" fill="none" stroke="#fff" stroke-width="1.4"/>
          </svg>
          <span>info@deedpaperlane.com</span>
        </li>
        <li class="contact__item">
          <svg class="contact__icon" viewBox="0 0 24 24" aria-hidden="true">
            <circle cx="12" cy="12" r="11" fill="#ec2229"/>
            <g fill="none" stroke="#fff" stroke-width="1.2">
              <circle cx="12" cy="12" r="6"/>
              <ellipse cx="12" cy="12" rx="2.6" ry="6"/>
              <path d="M6 12h12M7 9h10M7 15h10"/>
            </g>
          </svg>
          <span>www.deedpaperlane.com</span>
        </li>
      </ul>
      <p class="contact__address">87 Orchard Row, Suite 4<br>43210, Ohio</p>
    </div>
  </section>

  <section class="card card--back" aria-label="Card back">
    <div class="back">
      <p class="back__tagline">WE HELP PEOPLE LIVE!</p>
      <p class="back__brand">DEEDPAPER</p>
      <p class="back__descriptor">NOTE BUYERS</p>
      <p class="back__message">No more Tentants<br>No more Toilets</p>
      <p class="back__message back__message--cash">More Time, More Cash</p>
    </div>
  </section>
</body>
</html>
```